Electronic Time-sheet for phones

I need a time-sheet that can be accessed on the phone, be completed, then have the ability to electronically sign. The time sheet needs to be used two fold for supervision to verify hours and quantities and also for the client to be able to electronically sign. The time-sheet should be daily or weekly if we can get the data to fit. We are trying to streamline field supervisors having to log on to a computer to access a server just to do time-sheets. We need it to be user friendly. We need to have two places to have electronic signatures. One for supervisor or authorized representative and the other for the client to sign.

Target Market(s)

Industrial clients

Industry/Entity Type

Oil And Gas

Requirements
Must have
• hours, quantities, project name, location, signature line etc
Nice to have
• n/a
Should not have
• n/a

```html
<!DOCTYPE html>
<html lang="en">
<head>
<meta charset="utf-8">
<title>Supervisor: Available Actions</title>
<link href="https://fonts.googleapis.com/css2?family=Arimo:wght@400;700&family=Mulish:wght@300&display=swap" rel="stylesheet">
<style>
  :root {
    --navy: #10284f;
    --ink: #333333;
    --text: #555555;
    --muted: #777777;
    --blue: #1a85ff;
    --green: #2e9a3a;
    --red: #e0344b;
    --line: #c9c9c9;
    --tab-grey: #9a9a9a;
    --bg: #ffffff;
    --bar: #fafafa;
  }
  * { box-sizing: border-box; margin: 0; padding: 0; }
  html, body { width: 1200px; height: 1000px; overflow: hidden; background: var(--bg); }
  body { position: relative; font-family: "Arimo", Arial, sans-serif; color: var(--text); }

  /* ---------- Annotation column ---------- */
  .step-badge {
    position: absolute; left: 254px; top: 111px; width: 46px; height: 46px;
    border-radius: 50%; background: var(--navy); color: #fff;
    font-size: 14px; line-height: 46px; text-align: center;
  }
  .section-title {
    position: absolute; left: 160px; top: 182px;
    font-family: "Mulish", Arial, sans-serif; font-weight: 300;
    font-size: 30px; line-height: 38px; color: #111;
  }
  .action-list { position: absolute; left: 163px; top: 280px; width: 360px; }
  .action { margin-bottom: 8px; }
  .action-name {
    display: flex; align-items: center; gap: 8px;
    font-weight: 700; font-size: 14px; color: var(--text); height: 18px;
  }
  .action-name svg { width: 18px; height: 18px; flex: none; }
  .action-desc { margin-left: 27px; margin-top: 4px; font-size: 14px; line-height: 16px; color: var(--text); }

  /* ---------- App screen ---------- */
  .screen {
    position: absolute; left: 569px; top: 142px; width: 410px; height: 693px;
    border: 1px solid #bbb; background: #fff; overflow: hidden;
  }
  .status-bar {
    position: absolute; left: 0; top: 0; width: 100%; height: 20px;
    font-size: 12px; color: #000; display: flex; align-items: center; padding: 0 6px;
  }
  .status-bar .carrier { flex: 1; }
  .status-bar .clock { flex: 1; text-align: center; }
  .status-bar .power { flex: 1; display: flex; justify-content: flex-end; align-items: center; gap: 4px; }
  .battery { width: 24px; height: 10px; border: 1px solid #000; border-radius: 2px; padding: 1px; }
  .battery span { display: block; width: 55%; height: 100%; background: #000; }

  .back-link { position: absolute; left: 16px; top: 44px; font-size: 18px; color: var(--blue); }
  .brand {
    position: absolute; right: 16px; top: 38px;
    font-weight: 700; font-size: 28px; letter-spacing: 1px; color: var(--navy);
  }

  .sheet-card {
    position: absolute; left: 17px; top: 98px; width: 375px; height: 527px;
    border: 1px solid var(--line); border-radius: 6px;
  }
  .sheet-head {
    position: absolute; left: 13px; top: 18px; width: 349px; height: 43px;
    border-bottom: 1px solid #aaa; display: flex; align-items: flex-start;
  }
  .sheet-date { display: flex; align-items: center; gap: 8px; font-size: 15px; color: var(--ink); margin-top: 3px; }
  .sheet-date svg { width: 20px; height: 26px; }
  .add-employee {
    margin-left: auto; width: 161px; height: 33px; border-radius: 5px;
    background: var(--blue); color: #fff; font-size: 15px; line-height: 33px; text-align: center;
  }
  .column-heads { position: absolute; left: 13px; top: 82px; font-weight: 700; font-size: 15px; color: var(--text); }
  .column-heads span:last-child { position: absolute; left: 175px; white-space: nowrap; }

  .employee-row {
    position: absolute; left: 13px; width: 347px; height: 41px;
    border: 1.5px solid var(--line); border-radius: 4px;
    font-size: 15px; color: var(--ink); line-height: 38px; padding-left: 10px;
  }
  .row-actions { position: absolute; left: 175px; top: 9px; display: flex; gap: 20px; }
  .row-actions svg { width: 18px; height: 20px; }

  .sheet-details { position: absolute; left: 13px; top: 430px; color: var(--text); }
  .sheet-details h3 { font-weight: 400; font-size: 15px; margin-bottom: 3px; }
  .sheet-details p { font-size: 12px; line-height: 16px; }

  .tab-bar {
    position: absolute; left: 0; bottom: 0; width: 100%; height: 54px;
    border-top: 1px solid #e6e6e6; background: var(--bar); display: flex;
  }
  .tab { flex: 1; display: flex; flex-direction: column; align-items: center; padding-top: 7px; font-size: 8px; color: var(--text); }
  .tab svg { width: 30px; height: 30px; margin-bottom: 2px; }
  .tab.is-active { color: var(--blue); }
</style>
</head>
<body>

<svg width="0" height="0" style="position:absolute">
  <defs>
    <symbol id="icon-eye" viewBox="0 0 24 24"><path d="M1 12c3-5 7-7.5 11-7.5S20 7 23 12c-3 5-7 7.5-11 7.5S4 17 1 12z" fill="#1a85ff"/><circle cx="12" cy="12" r="4.5" fill="#fff"/><circle cx="12" cy="12" r="2.6" fill="#1a85ff"/></symbol>
    <symbol id="icon-export" viewBox="0 0 24 24"><path d="M7 2h8l5 5v4" fill="none" stroke="#2e9a3a" stroke-width="2"/><path d="M7 2 3 6v16h14v-5" fill="none" stroke="#2e9a3a" stroke-width="2"/><path d="M12 14h8M17 11l3 3-3 3" fill="none" stroke="#2e9a3a" stroke-width="2"/></symbol>
    <symbol id="icon-edit" viewBox="0 0 24 24"><path d="M18 12v9H3V6h9" fill="none" stroke="#1a85ff" stroke-width="1.6"/><path d="M9 15l1-4 9-9 3 3-9 9z" fill="none" stroke="#1a85ff" stroke-width="1.6"/></symbol>
    <symbol id="icon-trash" viewBox="0 0 24 24"><path d="M3 5h18M9 5V2.5h6V5M5 5l1.3 17h11.4L19 5" fill="none" stroke="#e0344b" stroke-width="1.8"/><path d="M10 9v10M14 9v10" stroke="#e0344b" stroke-width="1.6"/></symbol>
  </defs>
</svg>

<!-- Annotation column -->
<div class="step-badge">4.1</div>
<h1 class="section-title">Supervisor:<br>Available Actions</h1>

<div class="action-list">
  <div class="action">
    <div class="action-name"><svg><use href="#icon-eye"/></svg>View Time-sheet</div>
    <p class="action-desc">On clicking this icon, the time-sheet<br>will be displayed in read-only view. This<br>is where the actual time-sheet data is being<br>saved for an employee. It can be opened<br>in a pop-up window on this same screen. Or<br>opened in a new page in the app.</p>
  </div>
  <div class="action">
    <div class="action-name"><svg><use href="#icon-export"/></svg>Export Time-sheet</div>
    <p class="action-desc">On clicking this icon, the time-sheet<br>can be exported into a pdf and stored<br>on the smartphone. So the user can access<br>that pdf without launching this application.<br>In case of android phones, stored files<br>can be accessed through a file manager.<br>Alternatively, an email option can be provided<br>here. Or if a weekly email is required, then<br>email feature can be given at screen 3.</p>
  </div>
  <div class="action">
    <div class="action-name"><svg><use href="#icon-edit"/></svg>Edit Time-sheet</div>
    <p class="action-desc">Allows supervisor to make changes to<br>timesheet. You can also provide an option<br>to lock a sheet, i.e. once a sheet has been<br>signed, it cannot be edited or deleted.<br>This is just a suggestion.</p>
  </div>
  <div class="action">
    <div class="action-name"><svg><use href="#icon-trash"/></svg>Delete Time-sheet</div>
    <p class="action-desc">Removes the employee's time-sheet.</p>
  </div>
</div>

<!-- App screen -->
<main class="screen">
  <div class="status-bar">
    <span class="carrier">●●●○○ GS</span>
    <span class="clock">9:41 AM</span>
    <span class="power">58 % <span class="battery"><span></span></span></span>
  </div>

  <a class="back-link">‹ Go Back</a>
  <div class="brand">KESTREL</div>

  <section class="sheet-card">
    <div class="sheet-head">
      <div class="sheet-date">
        <svg viewBox="0 0 20 26"><path d="M6 1h13v24H1V6z" fill="none" stroke="#aaa" stroke-width="2"/></svg>
        5 November, 2018
      </div>
      <div class="add-employee">Add New Employee</div>
    </div>

    <div class="column-heads"><span>Employee Name</span><span>Actions</span></div>

    <div class="employee-row" style="top:121px">Jason Doe
      <div class="row-actions"><svg><use href="#icon-eye"/></svg><svg><use href="#icon-export"/></svg><svg><use href="#icon-edit"/></svg><svg><use href="#icon-trash"/></svg></div></div>
    <div class="employee-row" style="top:184px">John Doe
      <div class="row-actions"><svg><use href="#icon-eye"/></svg><svg><use href="#icon-export"/></svg><svg><use href="#icon-edit"/></svg><svg><use href="#icon-trash"/></svg></div></div>
    <div class="employee-row" style="top:247px">Jack Doe
      <div class="row-actions"><svg><use href="#icon-eye"/></svg><svg><use href="#icon-export"/></svg><svg><use href="#icon-edit"/></svg><svg><use href="#icon-trash"/></svg></div></div>
    <div class="employee-row" style="top:310px">Arthur Milne
      <div class="row-actions"><svg><use href="#icon-eye"/></svg><svg><use href="#icon-export"/></svg><svg><use href="#icon-edit"/></svg><svg><use href="#icon-trash"/></svg></div></div>
    <div class="employee-row" style="top:373px">Mike Tolland
      <div class="row-actions"><svg><use href="#icon-eye"/></svg><svg><use href="#icon-export"/></svg><svg><use href="#icon-edit"/></svg><svg><use href="#icon-trash"/></svg></div></div>

    <div class="sheet-details">
      <h3>Details for this time sheet:</h3>
      <p>Total Employees: 5<br>Last modified time sheet: Jack Doe<br>Last modified on: 5 November, 2018</p>
    </div>
  </section>

  <nav class="tab-bar">
    <div class="tab is-active">
      <svg viewBox="0 0 30 30"><path d="M12 4h11v23H7V9z" fill="none" stroke="#1a85ff" stroke-width="2.2"/></svg>
      Current Week
    </div>
    <div class="tab">
      <svg viewBox="0 0 30 30"><path d="M5 15a10 10 0 1 1 3 7" fill="none" stroke="#9a9a9a" stroke-width="2"/><path d="M2 13l3 3 3-3" fill="none" stroke="#9a9a9a" stroke-width="2"/><rect x="11" y="10" width="8" height="10" fill="#9a9a9a"/></svg>
      History
    </div>
    <div class="tab">
      <svg viewBox="0 0 30 30"><path d="M9 8a10 10 0 1 0 12 0" fill="none" stroke="#9a9a9a" stroke-width="2.4"/><path d="M15 3v11" stroke="#9a9a9a" stroke-width="2.4"/></svg>
      Logout
    </div>
  </nav>
</main>

</body>
</html>
```